Business Card Design for an international medical business

We need a professional and elegant business card design with fashionable graphic element. Our company is located in Hong Kong with three worldwide production lines for medical equipment(surgical face masks, N95, face shields and so on). Our factories all contain medical standard ISOs and all product fulfill Garrow lab and KTR testing standards.

We would like to see designs that show the impression of our professional expertise, formal corporate image with creative thinking work style and inspiring global concept. We want the content in both English and Japanese on the same card. We also want to print our the patent trade mark and company logo on the card.

Target Market(s)

Southeast Asia, US, EU

Industry/Entity Type

Medical Equipment

Contact Information for Business Card

Below are the content we want to be shown on the business card(please help us to simplified them to be more presentable and readable):

Company name: Brightmoor (Hong Kong) 5K Medical Technology Company Limited
Address: Unit 2204, 22/F, Pine Court, No.8 Ferndale Road, Kwun Lam, Hong Kong.
Band Name: B5K
Homepage: www.brightmoor5kq.com
Name: Lok Wing Fei
Title: Manager
Tel: +852-xxxx-xxxx
Mobile: +852-xxxx-xxxx
Email: xx@brightmoor5kq.com

Production Lines:
China: Ping Shan Kai Lok Medical Technology Company Limited
Mo Tan City Ren Bo Textile Machinery Company Limited
Bangladesh: B5K Medical Technology Company Limited

Qualifications:
ISO 13485:2016
ISO 14644-1:2015
ISO Class 8 Cleanroom
ASTM F2100 Level 2
EN14683 Type IIR
EN149 FFP2
CE Certified
FDA Registration number: XXX

Requirements
Must have
• use pantone color for the design
and provide the pantone number for printing purpose
Should not have
• Background color should not be black.

```html
<!DOCTYPE html>
<html lang="en">
<head>
<meta charset="utf-8">
<title>Brightmoor Business Card</title>
<link rel="stylesheet" href="https://fonts.googleapis.com/css2?family=Poppins:wght@400;500;600;700;800&display=swap">
<style>
  :root {
    --brand-pink: #e8094f;
    --brand-teal: #14b4b0;
    --ink: #2a2a2a;
    --paper: #ffffff;
    --stage: #e9eaec;
    --tint-pink: #fde6ec;
    --tint-teal: #e6f6f6;
  }
  * { box-sizing: border-box; margin: 0; padding: 0; }
  html, body { width: 1200px; height: 800px; overflow: hidden; }
  body {
    background: var(--stage);
    font-family: "Poppins", sans-serif;
    color: var(--ink);
    position: relative;
  }
  .card {
    position: absolute;
    width: 560px;
    height: 320px;
    background: var(--paper);
    border-radius: 22px;
    overflow: hidden;
    box-shadow: 0 10px 30px rgba(0,0,0,0.12);
  }
  .card--front { left: 60px; top: 70px; }
  .card--back { left: 580px; top: 410px; }

  .decor-circle {
    position: absolute;
    border-radius: 50%;
  }

  /* front */
  .brand-panel {
    position: absolute; left: 0; top: 0; bottom: 0; width: 170px;
    background: var(--brand-pink);
    display: flex; align-items: center; justify-content: center;
  }
  .brand-lockup {
    display: flex; align-items: center; gap: 10px;
    transform: rotate(-90deg);
    white-space: nowrap;
  }
  .brand-dot { width: 16px; height: 16px; border-radius: 50%; background: var(--paper); }
  .brand-name { color: var(--paper); font-weight: 700; font-size: 30px; letter-spacing: 2px; }

  .contact-block { position: absolute; left: 198px; top: 40px; right: 20px; }
  .person-name { font-weight: 700; font-size: 20px; letter-spacing: 0.5px; line-height: 1.1; }
  .person-name .family { color: var(--brand-pink); }
  .person-name .given { color: var(--brand-teal); }
  .person-title { font-size: 12px; margin-bottom: 14px; }
  .company-name { font-size: 11px; font-weight: 500; text-transform: uppercase; line-height: 1.45; margin-bottom: 10px; }
  .address { font-size: 11.5px; line-height: 1.45; margin-bottom: 12px; }
  .contact-list { list-style: none; font-size: 11.5px; line-height: 1.6; }
  .contact-list li { display: flex; align-items: center; gap: 8px; }
  .contact-icon { width: 15px; height: 15px; flex: none; }
  .website { color: var(--brand-pink); font-size: 13px; font-weight: 500; margin-top: 8px; }

  /* back */
  .cert-badge {
    position: absolute; left: 36px; top: 90px; width: 92px; height: 150px;
    border-radius: 12px;
    background: var(--brand-pink);
  }
  .production-block { position: absolute; left: 160px; top: 34px; right: 20px; font-size: 11.5px; line-height: 1.5; }
  .section-label { color: var(--brand-pink); font-weight: 700; font-size: 12px; text-transform: uppercase; }
  .footer-strip {
    position: absolute; left: 0; right: 0; bottom: 0; height: 10px;
    background: var(--brand-teal);
  }
  .web-tab {
    position: absolute; right: 0; bottom: 0; width: 240px; height: 72px;
    background: var(--brand-pink);
    border-top-left-radius: 40px;
    display: flex; align-items: center; justify-content: center;
    color: var(--paper); font-size: 13px; font-weight: 500;
  }
</style>
</head>
<body>

<section class="card card--front" aria-label="Business card front">
  <span class="decor-circle" style="right:-60px; top:-50px; width:260px; height:260px; background:var(--tint-teal);"></span>
  <span class="decor-circle" style="right:60px; top:-40px; width:90px; height:90px; background:var(--tint-pink);"></span>

  <div class="brand-panel">
    <div class="brand-lockup">
      <span class="brand-dot"></span>
      <span class="brand-name">BRIGHTMOOR</span>
    </div>
  </div>

  <div class="contact-block">
    <h1 class="person-name"><span class="family">LOK</span> <span class="given">WING FEI</span></h1>
    <p class="person-title">Manager</p>
    <p class="company-name">Brightmoor (Hong Kong)<br>5K Medical Technology Company Limited</p>
    <p class="address">Unit 2204, 22/F, Pine Court,<br>No.8 Ferndale Road,<br>Kwun Lam, Hong Kong.</p>
    <ul class="contact-list">
      <li>
        <svg class="contact-icon" viewBox="0 0 16 16" aria-hidden="true"><circle cx="8" cy="8" r="8" fill="#14b4b0"/><path d="M5.2 4.2l1.5 0 .6 1.8-1 .7a6 6 0 0 0 3 3l.7-1 1.8.6 0 1.5c-3.6.3-7-3-6.6-6.6z" fill="#fff"/></svg>
        +852-xxxx-xxxx
      </li>
      <li>
        <svg class="contact-icon" viewBox="0 0 16 16" aria-hidden="true"><circle cx="8" cy="8" r="8" fill="#e8094f"/><rect x="5.5" y="3.5" width="5" height="9" rx="1" fill="#fff"/><rect x="6.5" y="4.8" width="3" height="5.6" fill="#e8094f"/></svg>
        +852-xxxx-xxxx
      </li>
      <li>
        <svg class="contact-icon" viewBox="0 0 16 16" aria-hidden="true"><circle cx="8" cy="8" r="8" fill="#14b4b0"/><rect x="4" y="5" width="8" height="6" rx="0.8" fill="#fff"/><path d="M4.3 5.4L8 8.3l3.7-2.9" stroke="#14b4b0" stroke-width="0.9" fill="none"/></svg>
        xx@brightmoor5kq.com
      </li>
    </ul>
    <p class="website">www.brightmoor5kq.com</p>
  </div>
</section>

<section class="card card--back" aria-label="Business card back">
  <span class="decor-circle" style="right:-40px; top:-60px; width:260px; height:260px; background:var(--tint-teal);"></span>
  <span class="decor-circle" style="left:260px; top:-40px; width:80px; height:80px; background:var(--tint-pink);"></span>

  <div class="cert-badge" role="img" aria-label="Certification badge"></div>

  <div class="production-block">
    <p class="section-label">China:</p>
    <p>Ping Shan Kai Lok Medical Technology Company Limited</p>
    <p>Mo Tan City Ren Bo Textile Machinery Company Limited</p>
    <p class="section-label">Bangladesh:</p>
    <p>B5K Medical Technology Company Limited</p>
    <p class="section-label">Qualifications:</p>
    <p>ISO 13485:2016 | ISO 14644-1:2015 | ISO Class 8 Cleanroom</p>
    <p>ASTM F2100 Level 2 | EN14683 Type IIR | EN149 FFP2</p>
    <p>CE Certified</p>
    <p>FDA Registration number: XXX</p>
  </div>

  <div class="footer-strip"></div>
  <div class="web-tab">www.brightmoor5kq.com</div>
</section>

</body>
</html>
```